Vital Spark Electrical in need of a business card design

We need a new business card designed for our electrical business. We have a logo already which I will attach below.
Would like the business card to be..
-BLACK background preferably, possibly white back ground behind logo if colours clash.
-White & Blue (logo blue) text
Something that makes the logo pop, & a modern look. Possibly minimal clean format.

REQUIRE:
-Logo on front & back

TEXT TO INCLUDE (ON ONE SIDE):

Tom Harlow
Director/Electrician
M: 0417 365 208
E:info@vitalsparkelectrical-example.com.au
W:www.vitalsparkelectrical-example.com.au
R.E.C 57318

Custom/New Homes
Renovations
Commercial Office/Shop Fit-outs
Communications & Security Cameras
Electric Vehicle Chargers
Airconditioning
Updates

Requirements
Nice to have
• Possibly even lighten the grey shades for the words 'Vital' & 'Spark' to be more easily read on a black background.

```html
<!DOCTYPE html>
<html lang="en">
<head>
<meta charset="utf-8">
<title>Vital Spark Electrical – Business Card</title>
<link href="https://fonts.googleapis.com/css2?family=Open+Sans:wght@400;600;700&display=swap" rel="stylesheet">
<style>
  :root {
    --backdrop: #5e5e5e;
    --card-black: #000000;
    --card-white: #ffffff;
    --brand-blue: #16a3dd;
    --slate-dark: #333f4a;
    --slate-mid: #5c6670;
    --ink: #4a5560;
    --divider: #3c4650;
  }
  * { margin: 0; padding: 0; box-sizing: border-box; }
  html, body {
    width: 1200px; height: 1200px; overflow: hidden;
    background: var(--backdrop);
    font-family: "Open Sans", Arial, sans-serif;
  }
  .canvas { position: relative; width: 1200px; height: 1200px; }

  .card {
    position: absolute; left: 240px; width: 720px; height: 420px;
    border-radius: 22px; overflow: hidden;
  }

  /* Front */
  .card-front { top: 142px; background: var(--card-black); }
  .front-mark {
    position: absolute; left: 40px; top: 120px;
    width: 120px; height: 120px; background: var(--brand-blue);
  }
  .front-divider {
    position: absolute; left: 245px; top: 126px;
    width: 3px; height: 108px; background: var(--divider);
  }
  .front-name {
    position: absolute; left: 278px; top: 118px;
    color: var(--card-white); font-weight: 600; line-height: 1;
  }
  .front-name .line-main { display: block; font-size: 60px; letter-spacing: -0.5px; }
  .front-name .line-sub { display: block; font-size: 28px; letter-spacing: 21px; margin-top: 12px; }
  .front-web {
    position: absolute; left: 0; right: 0; top: 360px;
    text-align: center; font-size: 21px; color: var(--card-white);
  }
  .front-web .domain { color: var(--brand-blue); }

  /* Back */
  .card-back { top: 638px; background: var(--card-white); }
  .person-name {
    position: absolute; left: 24px; top: 22px;
    font-size: 25px; font-weight: 700; color: var(--ink);
  }
  .person-name .surname { color: var(--brand-blue); }
  .person-role {
    position: absolute; left: 24px; top: 56px;
    font-size: 16px; color: var(--brand-blue);
  }
  .contacts { position: absolute; left: 24px; top: 108px; list-style: none; }
  .contacts li {
    display: flex; align-items: center; gap: 10px;
    height: 29.5px; font-size: 17px; color: var(--ink);
  }
  .contacts svg { width: 19px; height: 19px; fill: var(--brand-blue); }

  .services {
    position: absolute; top: 276px; list-style: none;
  }
  .services.col-left { left: 24px; }
  .services.col-right { left: 374px; }
  .services li {
    display: flex; align-items: center; gap: 9px;
    height: 29.5px; font-size: 17px; color: var(--ink);
  }
  .services li::before {
    content: ""; width: 12px; height: 12px; border-radius: 50%;
    background: var(--brand-blue); flex: none;
  }

  .back-name {
    position: absolute; right: 28px; top: 44px; width: 260px;
    text-align: right; color: var(--brand-blue);
    font-weight: 700; font-size: 46px; line-height: 1.08;
  }

  .footer-band {
    position: absolute; left: 0; bottom: 0; width: 720px; height: 40px;
    display: flex;
  }
  .footer-band .band-blue { width: 480px; background: var(--brand-blue); }
  .footer-band .band-gap { width: 2px; background: var(--card-white); }
  .footer-band .licence {
    width: 168px; background: var(--slate-mid); color: var(--card-white);
    font-size: 17px; display: flex; align-items: center; justify-content: center;
  }
  .footer-band .band-dark { flex: 1; background: var(--slate-dark); }
</style>
</head>
<body>
<main class="canvas">

  <section class="card card-front">
    <div class="front-mark"></div>
    <div class="front-divider"></div>
    <div class="front-name">
      <span class="line-main">Vital Spark</span>
      <span class="line-sub">Electrical</span>
    </div>
    <p class="front-web">www.<span class="domain">vitalsparkelectrical-example</span>.com.au</p>
  </section>

  <section class="card card-back">
    <h1 class="person-name">Tom <span class="surname">Harlow</span></h1>
    <p class="person-role">Director/Electrician</p>

    <ul class="contacts">
      <li>
        <svg viewBox="0 0 24 24" aria-hidden="true"><path d="M6.6 10.8a15.1 15.1 0 0 0 6.6 6.6l2.2-2.2c.3-.3.7-.4 1-.2 1.1.4 2.3.6 3.6.6.6 0 1 .4 1 1V20c0 .6-.4 1-1 1C10.6 21 3 13.4 3 4c0-.6.4-1 1-1h3.5c.6 0 1 .4 1 1 0 1.3.2 2.5.6 3.6.1.3 0 .7-.2 1z"/></svg>
        0417 365 208
      </li>
      <li>
        <svg viewBox="0 0 24 24" aria-hidden="true"><path d="M2 5h20v14H2z M3.5 6.5 12 13l8.5-6.5" fill="none" stroke="#16a3dd" stroke-width="0"/><path d="M2 5h20v14H2V5zm2 2v.4l8 5.6 8-5.6V7H4z"/></svg>
        info@vitalsparkelectrical-example.com.au
      </li>
      <li>
        <svg viewBox="0 0 24 24" aria-hidden="true"><circle cx="12" cy="12" r="9.5"/><path d="M3 12h18M12 2.5c3 3 3 16 0 19M12 2.5c-3 3-3 16 0 19" stroke="#fff" stroke-width="1.4" fill="none"/></svg>
        www.vitalsparkelectrical-example.com.au
      </li>
    </ul>

    <div class="back-name">Vital Spark Electrical</div>

    <ul class="services col-left">
      <li>Custom/New Homes</li>
      <li>Renovations</li>
      <li>Commercial Office/Shop Fit-outs</li>
    </ul>
    <ul class="services col-right">
      <li>Communications &amp; Security Cameras</li>
      <li>Electric Vehicle Chargers</li>
      <li>Airconditioning</li>
    </ul>

    <div class="footer-band">
      <div class="band-blue"></div>
      <div class="band-gap"></div>
      <div class="licence">R.E.C 57318</div>
      <div class="band-gap"></div>
      <div class="band-dark"></div>
    </div>
  </section>

</main>
</body>
</html>
```